Professionelles Social Media Material für Reinigungsdienstleister
Schnelle und unkomplizierte Abwicklung - Briefing wurde nach Wünschen umgesetzt und entsprach direkt den Vorstellungen!
Zielgruppe
Wir reinigen Privathaushalte, Ferienwohnungen, Arztpraxen und Büroräume.
Aufgabenstellung
Ich wünsche Material für ein professionelles Auftreten bei Facebook und Instagram. Wir müssen bei Facebook leider neu starten und haben Instagram bei dieser Firma bisher vernachlässigt.
Nun wollen wir unser Social Media professionell erscheinen lassen und einen Plan für die kommenden 2 Monate erstellen. Wir suchen dafür mindestens 20 passende Postings und die Inhalte für den Start.
Nachtrag zu den Postings: Wir wollen ganz allgemeinen Content und sind offen für alle Vorschläge. Es kann gern auch eine Sommeraktion beworben werden, bei der wir Neukunden 100€ schenken und eine Aktion, bei der es eine kostenlose Erstreinigung gibt um unsere Leistung zu testen.

```html
<!DOCTYPE html>
<html lang="de">
<head>
<meta charset="utf-8">
<title>Putzwerk Pioniere – Social Media Posts</title>
<link href="https://fonts.googleapis.com/css2?family=Montserrat:ital,wght@0,400;0,500;0,600;0,700;0,800;0,900;1,600;1,700;1,800&display=swap" rel="stylesheet">
<style>
  :root{
    --page:#dcdcdc;
    --white:#ffffff;
    --blue:#6fa6ca;
    --blue-light:#a9cbe2;
    --blue-text:#2f7cb8;
    --navy:#38466f;
    --yellow:#f4dc5a;
    --grey:#9a9a9a;
  }
  *{box-sizing:border-box;margin:0;padding:0}
  html,body{width:825px;height:1200px;overflow:hidden;background:var(--page);font-family:"Montserrat",sans-serif}
  .sheet{position:relative;width:825px;height:1200px}
  .post{position:absolute;width:165px;height:208px;background:var(--white);overflow:hidden;box-shadow:1px 2px 3px rgba(0,0,0,.18)}
  .hdr{position:absolute;left:52px;top:0;right:0;height:56px;background:var(--blue);border-radius:30px 0 0 60px/30px 0 0 45px}
  .title{position:absolute;left:58px;top:11px;color:var(--white);font-weight:800;font-size:12.5px;line-height:.98;letter-spacing:.2px;z-index:3}
  .logo{position:absolute;left:4px;top:8px;width:44px;text-align:center;color:var(--navy);font-weight:700;font-size:5.2px;line-height:1.1;z-index:3}
  .logo i{display:block;width:10px;height:10px;margin:0 auto 2px;background:var(--navy)}
  .pill{position:absolute;left:32px;top:54px;width:140px;height:34px;background:var(--yellow);border-radius:50%;color:var(--blue-text);font-style:italic;font-weight:800;font-size:8.2px;line-height:1.05;padding:9px 0 0 24px;z-index:2}
  .band{position:absolute;left:0;right:0;bottom:0;background:var(--blue);border-radius:0 70px 0 0/0 24px 0 0}
  .foot{position:absolute;left:30px;color:var(--white);font-size:5.8px;font-weight:600;line-height:1.35;z-index:3}
  .foot.it{font-style:italic;font-weight:500}
  .ph{position:absolute;z-index:1}
  .side{position:absolute;color:var(--blue-text);font-size:5.8px;font-weight:600;line-height:1.3;z-index:3}
  .bubble{position:absolute;border:1.3px solid var(--blue-light);border-radius:50%;background:var(--white)}
  .bq{position:absolute;font-size:6.2px;line-height:1.35;color:var(--blue-text);font-weight:500;z-index:3}
  .bq b{font-weight:700}
  .quote{position:absolute;color:var(--blue);font-weight:900;font-size:30px;font-style:italic;line-height:1;z-index:3}
  .dot{position:absolute;border-radius:50%}
  .star{position:absolute;width:10px;height:10px;z-index:3}
</style>
</head>
<body>
<main class="sheet">

<!-- Row 1 -->
<article class="post" style="left:39px;top:24px">
  <div class="hdr"></div><div class="logo"><i></i>Putzwerk<br>Pioniere</div>
  <h2 class="title">REINIGUNGS<br>SERVICE</h2>
  <div class="band" style="height:72px"></div>
  <div class="pill" style="left:32px;width:138px">Sauberkeit ist unsere<br>Leidenschaft</div>
  <div class="ph" role="img" aria-label="Heldin mit Maske und bunten Staubwedeln" style="left:16px;top:84px;width:142px;height:72px;border-radius:40% 50% 30% 50%;background:linear-gradient(120deg,#c0453c,#e9b9a0 45%,#f2d35a 75%,#d98fb6);z-index:2"></div>
  <p class="side" style="left:8px;top:94px;transform:rotate(-16deg);font-style:italic;font-weight:500">Jetzt<br>Angebot<br>einholen!</p>
  <p class="foot" style="top:172px">Das bisschen<br>Haushalt macht sich von allein ..<br>Du brauchst nur den <i><b>richtigen Helden!</b></i></p>
</article>

<article class="post" style="left:233px;top:24px">
  <div class="hdr"></div><div class="logo"><i></i>Putzwerk<br>Pioniere</div>
  <h2 class="title">REINIGUNGS<br>SERVICE</h2>
  <div class="band" style="height:76px"></div>
  <div class="pill" style="left:30px;width:110px;padding:0"></div>
  <div class="ph" role="img" aria-label="Drei Reinigungskräfte mit Staubsauger und Putzmitteln" style="left:62px;top:34px;width:100px;height:120px;border-radius:18px;background:linear-gradient(180deg,#c9a78f,#4d89bd 55%,#d7c23d);z-index:4"></div>
  <p class="side" style="left:14px;top:98px;font-style:italic;color:#7f8896">Zuverlässig,<br>pünktlich und<br>blitzsauber</p>
  <p class="foot it" style="top:168px">Wir sorgen für glanzvolle Ergebnisse<br>in privaten <b>Haushalten, Büros<br>und Gewerbe.</b></p>
</article>

<article class="post" style="left:427px;top:24px">
  <div class="hdr"></div><div class="logo"><i></i>Putzwerk<br>Pioniere</div>
  <h2 class="title">REINIGUNGS<br>SERVICE</h2>
  <div class="band" style="height:90px"></div>
  <div class="pill" style="left:32px;width:128px;padding:8px 0 0 26px;font-size:9.5px">Sommeraktion!</div>
  <div class="ph" role="img" aria-label="Überraschte Frau vor Strand und Himmel" style="left:8px;top:82px;width:156px;height:74px;border-radius:50%;background:linear-gradient(90deg,#a9cde6,#e4c9b4 40%,#cfe4f1 70%,#e6d2a8);z-index:2"></div>
  <p class="side" style="left:80px;top:96px;transform:rotate(-14deg);font-style:italic;font-weight:700;font-size:5.6px;z-index:4">Jeder<br>Neukunde<br>bekommt:<br><span style="font-size:8px">€ 100,-<br>GESCHENKT!</span></p>
  <p class="foot it" style="top:178px">Damit du entspannt in den Urlaub<br>fahren kannst!</p>
</article>

<article class="post" style="left:622px;top:24px">
  <div class="hdr"></div><div class="logo"><i></i>Putzwerk<br>Pioniere</div>
  <h2 class="title">REINIGUNGS<br>SERVICE</h2>
  <div class="band" style="height:26px;border-radius:0"></div>
  <div class="pill" style="left:32px;width:128px;padding:8px 0 0 26px">Checkliste:<br>&nbsp;&nbsp;&nbsp;&nbsp;&nbsp;Frühjahrsputz</div>
  <div class="ph" style="left:4px;top:88px;width:96px;height:70px;border-radius:50%;background:var(--blue)"></div>
  <p class="foot" style="left:33px;top:96px;font-weight:500;font-size:5.8px">Dinge, die beim<br>Frühjahrsputz<br>oft vergessen<br>werden ..<br><span style="font-size:7px">Wir vergessen<br>nichts!</span></p>
  <svg style="position:absolute;left:0;top:90px" width="165" height="100" viewBox="0 0 165 100" fill="none" stroke="#6fa6ca" stroke-width="1">
    <path d="M100 30 L114 25 M98 62 L114 56 M40 68 L30 82 M86 70 L94 76"/>
    <rect x="120" y="12" width="12" height="2" rx="1"/><rect x="120" y="16" width="12" height="2" rx="1"/><rect x="120" y="20" width="12" height="2" rx="1"/><rect x="120" y="24" width="12" height="2" rx="1"/>
    <rect x="122" y="40" width="10" height="22"/><path d="M122 51 H132 M127 40 V62"/>
    <rect x="22" y="92" width="6" height="12" rx="2"/>
    <rect x="88" y="96" width="7" height="10" rx="1"/>
  </svg>
  <p class="side" style="left:117px;top:117px;font-size:4.5px">Heizkörper</p>
  <p class="side" style="left:117px;top:155px;font-size:4.5px">Fensterrahmen</p>
  <p class="side" style="left:40px;top:168px;font-size:4.5px">Türgriffe</p>
  <p class="side" style="left:100px;top:168px;font-size:4.5px">Lichtschalter</p>
  <p class="foot it" style="left:30px;top:191px">Jetzt Angebot einholen!</p>
</article>

<!-- Row 2 -->
<article class="post" style="left:39px;top:254px">
  <div class="hdr"></div><div class="logo"><i></i>Putzwerk<br>Pioniere</div>
  <h2 class="title">REINIGUNGS<br>SERVICE</h2>
  <div class="band" style="height:80px"></div>
  <div class="pill" style="left:32px;width:136px">Glas- und<br>Fensterreinigung</div>
  <div class="ph" role="img" aria-label="Mann reinigt ein Fenster mit Abzieher" style="left:8px;top:92px;width:152px;height:64px;border-radius:24px 16px 40px 30px;background:linear-gradient(100deg,#d9ecf7,#b7d6ec 45%,#3a3f48 75%,#c9a58c);z-index:2"></div>
  <div class="ph" style="left:8px;top:90px;width:60px;height:14px;background:var(--blue);border-radius:3px;transform:rotate(-10deg);z-index:3"></div>
  <p class="foot" style="left:14px;top:89px;transform:rotate(-10deg);font-size:6.5px;line-height:1;z-index:4">garantiert<br><span style="font-size:4.5px">streifenfrei</span></p>
  <p class="foot" style="left:38px;top:178px;font-size:6.3px">Wir bringen Ihre Fenster<br>zum Strahlen!</p>
</article>

<article class="post" style="left:233px;top:254px">
  <div class="hdr"></div><div class="logo"><i></i>Putzwerk<br>Pioniere</div>
  <h2 class="title">REINIGUNGS<br>SERVICE</h2>
  <div class="pill" style="left:32px;width:136px;padding:12px 0 0 26px">was Kunden sagen:</div>
  <div class="bubble" style="left:30px;top:86px;width:150px;height:110px"></div>
  <svg style="position:absolute;left:30px;top:160px" width="20" height="30" viewBox="0 0 20 30"><path d="M8 0 L2 28 L18 12" fill="#fff" stroke="#a9cbe2" stroke-width="1.3"/></svg>
  <p class="quote" style="left:20px;top:92px">"</p>
  <p class="bq" style="left:58px;top:114px"><b><i>„Zuverlässig, pünktlich<br>und blitzsauber</i></b> –<br>ich empfehle euch gerne<br>weiter!" – Karin Lehmann<br>Wir sagen:<br>Danke für das Vertrauen!</p>
</article>

<article class="post" style="left:427px;top:254px">
  <div class="hdr"></div><div class="logo"><i></i>Putzwerk<br>Pioniere</div>
  <h2 class="title">REINIGUNGS<br>SERVICE</h2>
  <div class="band" style="height:80px"></div>
  <div class="pill" style="left:32px;width:128px;padding:10px 0 0 26px;font-style:normal;font-weight:700;font-size:6px;color:#b79e2c">Wir schenken dir<br>die Erstreinigung</div>
  <div class="ph" style="left:8px;top:88px;width:156px;height:56px;border-radius:28px;background:#5d97bf;z-index:2"></div>
  <div class="ph" role="img" aria-label="Lachende Frau mit gelber Jacke und Putzhandschuhen" style="left:88px;top:80px;width:66px;height:82px;border-radius:30px 30px 8px 8px;background:linear-gradient(180deg,#3a2a22,#c48d6b 40%,#e9c13a 75%,#e57da6);z-index:3"></div>
  <p class="foot" style="left:24px;top:126px;font-size:10px;font-weight:800">TESTE UNS!</p>
  <p class="foot" style="left:44px;top:178px;font-size:6.2px;font-weight:500">Erstreinigung gratis · <b>Jetzt<br>Angebot einholen!</b></p>
</article>

<article class="post" style="left:622px;top:254px">
  <div class="hdr"></div><div class="logo"><i></i>Putzwerk<br>Pioniere</div>
  <h2 class="title">REINIGUNGS<br>SERVICE</h2>
  <div class="pill" style="left:32px;width:136px;padding:12px 0 0 26px">WIR STELLEN EIN!</div>
  <div class="bubble" style="left:30px;top:90px;width:150px;height:106px"></div>
  <p class="quote" style="left:20px;top:92px">"</p>
  <p class="bq" style="left:58px;top:108px"><b>Wir suchen Verstärkung!</b><br>(m/w/d) <b>in Teilzeit<br>gesucht – fair bezahlt,<br>familiäres Team.</b><br>Sende uns deine<br>Bewerbung per Mail<br>oder ruf an!</p>
  <div class="dot" style="left:2px;top:198px;width:22px;height:22px;background:var(--blue)"></div>
  <div class="dot" style="left:60px;top:198px;width:22px;height:22px;background:var(--blue)"></div>
  <div class="dot" style="left:18px;top:186px;width:7px;height:7px;border:1px solid var(--blue)"></div>
  <div class="dot" style="left:46px;top:198px;width:4px;height:4px;background:var(--blue)"></div>
  <div class="dot" style="left:100px;top:196px;width:7px;height:7px;border:1px solid var(--blue)"></div>
</article>

<!-- Row 3 -->
<article class="post" style="left:39px;top:489px">
  <div class="hdr"></div><div class="logo"><i></i>Putzwerk<br>Pioniere</div>
  <h2 class="title">REINIGUNGS<br>SERVICE</h2>
  <div class="band" style="height:66px"></div>
  <div class="pill" style="left:32px;width:136px;padding:6px 0 0 50px;font-style:normal;font-weight:700;font-size:8.5px">Büroreinigung<br><i style="font-size:5px;font-weight:600">warum sie so wichtig ist</i></div>
  <div class="ph" role="img" aria-label="Frau streckt sich entspannt am Schreibtisch im Büro" style="left:8px;top:84px;width:146px;height:64px;border-radius:30px;background:linear-gradient(90deg,#eef2f5,#c6cfd6 30%,#c86b3a 50%,#eceff1 80%);z-index:2"></div>
  <div class="ph" style="left:108px;top:92px;width:56px;height:56px;border-radius:50%;background:var(--blue);z-index:3"></div>
  <p class="foot" style="left:112px;top:108px;font-size:3.6px;font-weight:500;text-align:center;width:48px;z-index:4">Wussten Sie, dass <b>saubere Arbeitsplätze</b> die <b>Produktivität</b> um 12 % steigern können?</p>
  <p class="foot" style="left:44px;top:175px;font-size:6.2px">Jetzt Reinigungsplan für Ihr<br>Büro erstellen lassen.</p>
</article>

<article class="post" style="left:233px;top:489px">
  <div class="hdr"></div><div class="logo"><i></i>Putzwerk<br>Pioniere</div>
  <h2 class="title">REINIGUNGS<br>SERVICE</h2>
  <div class="band" style="height:36px"></div>
  <div class="pill" style="left:32px;width:136px;padding:12px 0 0 26px">Spezialreinigung</div>
  <div class="ph" role="img" aria-label="Gekachelte Dusche mit Quietscheente" style="left:8px;top:90px;width:156px;height:76px;border-radius:36px;background:linear-gradient(180deg,#2c85b8,#6bb6d8 55%,#eef4f6);z-index:2"></div>
  <p class="foot" style="left:60px;top:96px;font-size:6.8px;font-weight:600;text-align:center">Schimmel in<br>der Dusche?</p>
  <div class="ph" style="left:12px;top:126px;width:70px;height:32px;border-radius:50%;background:var(--blue-light);z-index:3"></div>
  <p class="bq" style="left:16px;top:128px;font-size:3.8px;line-height:1.3;color:#2f6e9f;transform:rotate(-6deg)"><b>Kein Problem.</b> Wir über-<br>nehmen auch schwierige<br>Fälle – professionell und<br>hygienisch."</p>
  <p class="foot" style="left:34px;top:188px;font-size:6.2px">Jetzt Angebot einholen!</p>
</article>

<article class="post" style="left:427px;top:489px">
  <div class="hdr"></div><div class="logo"><i></i>Putzwerk<br>Pioniere</div>
  <h2 class="title">REINIGUNGS<br>SERVICE</h2>
  <div class="band" style="height:80px;border-radius:0 90px 0 0/0 30px 0 0"></div>
  <div class="pill" style="left:32px;width:136px;padding:10px 0 0 26px;font-style:normal;font-weight:700;font-size:7.6px">Umzugsreinigung,<br>Endreinigung</div>
  <p class="side" style="left:18px;top:100px;font-size:5px;text-align:right">Neuer Mieter,<br>neuer Glanz!</p>
  <div class="ph" role="img" aria-label="Umzugskartons mit Besen und Pflanzen" style="left:64px;top:92px;width:84px;height:66px;border-radius:8px;background:linear-gradient(180deg,#6c8a5e,#d7b287 45%,#c29a6c);z-index:2"></div>
  <p class="foot" style="left:32px;top:172px;font-size:3.8px;font-weight:500">Wir übernehmen die Endreinigung beim Umzug –<br>zuverlässig und gründlich.</p>
  <p class="foot" style="left:32px;top:189px;font-size:6.2px">Jetzt Angebot einholen!</p>
</article>

<article class="post" style="left:622px;top:489px">
  <div class="hdr"></div><div class="logo"><i></i>Putzwerk<br>Pioniere</div>
  <h2 class="title">REINIGUNGS<br>SERVICE</h2>
  <div class="pill" style="left:32px;width:136px;padding:11px 0 0 26px;font-size:9.5px">Umfrage</div>
  <div class="bubble" style="left:30px;top:90px;width:150px;height:106px"></div>
  <p class="quote" style="left:20px;top:92px">"</p>
  <p class="bq" style="left:58px;top:108px;font-weight:700"><span style="font-size:7px">Was ist für Sie<br>wichtiger?</span><br><br>A) Zeitersparnis<br>B) Hygiene<br>C) Umweltfreundlichkeit<br>Kommentieren Sie!</p>
  <div class="dot" style="left:5px;top:189px;width:7px;height:7px;background:var(--blue)"></div>
  <div class="dot" style="left:30px;top:202px;width:20px;height:20px;background:var(--blue)"></div>
  <div class="dot" style="left:84px;top:202px;width:20px;height:20px;background:var(--blue)"></div>
  <div class="dot" style="left:18px;top:198px;width:7px;height:7px;border:1px solid var(--blue)"></div>
  <div class="dot" style="left:70px;top:200px;width:4px;height:4px;background:var(--blue)"></div>
  <div class="dot" style="left:120px;top:200px;width:7px;height:7px;border:1px solid var(--blue)"></div>
</article>

<!-- Row 4 -->
<article class="post" style="left:39px;top:730px">
  <div class="hdr"></div><div class="logo"><i></i>Putzwerk<br>Pioniere</div>
  <h2 class="title">REINIGUNGS<br>SERVICE</h2>
  <div class="band" style="height:116px;border-radius:0"></div>
  <div class="pill" style="left:32px;width:136px;padding:7px 0 0 26px;font-style:normal;font-weight:500;font-size:6.6px;line-height:1.05;z-index:4">Werde <b><i>Lizenznehmer</i></b> –<br>Starte dein <b>eigenes<br>Business</b> mit erprobtem<br>Konzept</div>
  <p class="quote" style="left:4px;top:62px;z-index:5">"</p>
  <p class="foot" style="left:6px;top:102px;font-size:5.2px">Jetzt infor-<br>mieren &amp;<br>Teil unseres<br>Lizenz-<br>systems<br>werden!</p>
  <div class="bubble" style="left:40px;top:82px;width:170px;height:118px;z-index:2;border:none"></div>
  <p class="bq" style="left:42px;top:100px;font-size:5.3px;text-align:center;width:120px;line-height:1.55">● <b>Du möchtest</b><br>dich selbstständig machen,<br>aber nicht bei Null anfangen?<br><b>● Profitiere von unserem bewährten<br>Geschäftsmodell<br>● Schulung &amp; laufende Unterstützung<br>● Volle unternehmerische Frei-<br>heit mit starkem Netzwerk</b></p>
</article>

<article class="post" style="left:233px;top:730px">
  <div class="hdr"></div><div class="logo"><i></i>Putzwerk<br>Pioniere</div>
  <h2 class="title">REINIGUNGS<br>SERVICE</h2>
  <div class="band" style="height:34px"></div>
  <div class="pill" style="left:32px;width:136px;padding:7px 0 0 30px">Zeit für deinen<br>Neuanfang!</div>
  <div class="ph" role="img" aria-label="Lächelnder Mann mit erhobenem Daumen" style="left:4px;top:44px;width:40px;height:140px;border-radius:16px 16px 4px 4px;background:linear-gradient(180deg,#c9987a,#cb5a4c 30%,#93aed0 60%,#4f73a5);z-index:4"></div>
  <div class="bubble" style="left:44px;top:82px;width:140px;height:104px"></div>
  <p class="bq" style="left:50px;top:92px;font-size:5.5px">○ Du träumst davon, dein<br>&nbsp;&nbsp;<b>eigener Chef</b><br>&nbsp;&nbsp;zu sein?<br>○ Wir suchen<br>&nbsp;&nbsp;<b>engagierte Menschen</b> mit<br>&nbsp;&nbsp;<b>Unternehmergeist!</b><br><br>○ Keine Erfahrung?<br>&nbsp;&nbsp;Kein Problem –<br>&nbsp;&nbsp;wir bringen dir alles bei.</p>
  <p class="quote" style="left:128px;top:90px;font-size:24px">"</p>
  <p class="foot" style="left:82px;top:182px;font-size:5.8px">Interessiert? schreib<br>uns einfach direkt!</p>
</article>

<article class="post" style="left:427px;top:730px">
  <div class="hdr"></div><div class="logo"><i></i>Putzwerk<br>Pioniere</div>
  <h2 class="title">REINIGUNGS<br>SERVICE</h2>
  <div class="band" style="height:30px;border-radius:0"></div>
  <div class="pill" style="left:32px;width:136px;padding:5px 0 0 38px;font-style:normal;font-weight:500;font-size:7.6px">Reinigung ist mehr<br>als nur den Lappen<br>schwingen!</div>
  <div class="ph" style="left:-2px;top:74px;width:72px;height:80px;border-radius:50%;background:#3b78b6;z-index:2"></div>
  <p class="foot" style="left:10px;top:86px;font-size:5.5px;font-weight:500;line-height:1.1">Reinigung ist<br>Handwerk,<br>Service und<br>Leidenschaft<br>in einem.</p>
  <div class="ph" role="img" aria-label="Reinigungskraft mit Eimer und Putzmitteln" style="left:0;top:124px;width:56px;height:54px;border-radius:24px 24px 0 0;background:linear-gradient(180deg,#9ec5dd,#3aa0bf 55%,#e6c24a);z-index:3"></div>
  <p class="bq" style="left:70px;top:102px;font-size:4.1px;line-height:1.55">● Sorgfalt und Liebe zum Detail<br>● Fachwissen über Materialien<br>&nbsp;&nbsp;&nbsp;und Reinigungstechniken<br>● Verantwortung für Hygiene<br>&nbsp;&nbsp;&nbsp;und Gesundheit<br>● Organisationstalent und<br>&nbsp;&nbsp;&nbsp;Verlässlichkeit<br>● Kundenorientierung und<br>&nbsp;&nbsp;&nbsp;Vertrauen</p>
  <p class="foot" style="left:6px;top:181px;font-size:3.9px;font-weight:500">Unsere ‚Putzwerk Pioniere' sind echte Profis, die Räume nicht<br>nur sauber, sondern lebenswert machen.<br>Reinigung ist <b>Handwerk, Service und Leidenschaft</b> in einem.</p>
</article>

<article class="post" style="left:622px;top:730px">
  <div class="hdr"></div><div class="logo"><i></i>Putzwerk<br>Pioniere</div>
  <h2 class="title">REINIGUNGS<br>SERVICE</h2>
  <div class="band" style="height:44px"></div>
  <div class="ph" style="left:0;top:110px;width:110px;height:60px;border-radius:0 50px 50px 0;background:var(--blue)"></div>
  <div class="pill" style="left:32px;width:136px;padding:7px 0 0 26px">Sauberkeit jetzt<br>per App</div>
  <div class="ph" role="img" aria-label="Lachende Frau zeigt auf ein Smartphone" style="left:90px;top:86px;width:76px;height:84px;border-radius:36px 10px 0 36px;background:linear-gradient(160deg,#8a5a38,#e7b995 45%,#f3f1ee);z-index:2"></div>
  <p class="foot" style="left:10px;top:118px;font-size:5.3px;font-weight:500;line-height:1.2">Mit unserer<br>neuen Reini-<br>gungsfirma-App<br>haben Sie alles im<br>Griff – jederzeit<br>und überall</p>
  <p class="foot" style="left:32px;top:177px;font-size:6.3px">Jetzt kostenlos downloaden<br>und Zeit sparen!</p>
</article>

<!-- Row 5 -->
<article class="post" style="left:39px;top:968px">
  <div class="hdr"></div><div class="logo"><i></i>Putzwerk<br>Pioniere</div>
  <h2 class="title">REINIGUNGS<br>SERVICE</h2>
  <div class="band" style="height:44px;border-radius:0"></div>
  <div class="pill" style="left:32px;width:136px;padding:7px 0 0 26px">Sauberkeit darf nicht<br>illegal sein!</div>
  <div class="ph" style="left:0;top:64px;width:90px;height:100px;border-radius:60px 0 0 0;background:linear-gradient(135deg,#9ea6ae,#ffffff 70%)"></div>
  <div class="ph" role="img" aria-label="Silhouette einer Person beim Wischen" style="left:74px;top:88px;width:38px;height:78px;border-radius:16px 16px 4px 4px;background:#b7b7b7;z-index:2"></div>
  <p class="bq" style="left:6px;top:106px;font-size:4.8px;line-height:1.4">Schwarzarbeit gefähr-<br>det mehr als nur den Job,<br>man riskiert hohe Strafen<br>und verliert im Ernstfall<br>jede Absicherung und<br>das gilt auch<br>für Auftraggeber!</p>
  <p class="bq" style="left:104px;top:102px;font-size:4.2px;line-height:1.35;color:#3b4d74;z-index:3">• Kein Versicherungs-<br>&nbsp;&nbsp;schutz bei Schäden<br>• Keine Unfallabsiche-<br>&nbsp;&nbsp;rung<br>• Bußgelder bis zu<br>&nbsp;&nbsp;50.000 €<br>• Rechtsunsicherheit<br>&nbsp;&nbsp;bei Streitfällen</p>
  <p class="foot" style="left:14px;top:172px;font-size:5.6px;font-weight:500"><b><i>Tipp:</i></b> Immer auf <span style="color:var(--yellow)">offizielle Anbieter</span> mit <span style="color:var(--yellow)">Steuer-<br>nummer</span> und <span style="color:var(--yellow)">Rechnung</span> bestehen.<br><b style="color:var(--yellow)">Sauber. Sicher. Seriös – dafür stehen wir!</b></p>
</article>

<article class="post" style="left:233px;top:968px">
  <div class="hdr"></div><div class="logo"><i></i>Putzwerk<br>Pioniere</div>
  <h2 class="title">REINIGUNGS<br>SERVICE</h2>
  <div class="band" style="height:66px"></div>
  <div class="pill" style="left:32px;width:136px;padding:7px 0 0 26px">Sommer-Aktion<br>endet bald!</div>
  <div class="ph" role="img" aria-label="Überraschte Frau vor Strand und Himmel" style="left:8px;top:100px;width:150px;height:70px;border-radius:50%;background:linear-gradient(90deg,#a9cde6,#e4c9b4 40%,#cfe4f1 70%,#e6d2a8);z-index:2"></div>
  <svg style="position:absolute;left:106px;top:70px;z-index:4" width="52" height="52" viewBox="0 0 52 52"><circle cx="26" cy="26" r="24" fill="#fff" stroke="#38466f" stroke-width="2.5"/><circle cx="26" cy="26" r="19" fill="none" stroke="#38466f" stroke-width="1"/><path d="M26 26 V13 M26 26 L34 30" stroke="#38466f" stroke-width="1.6" stroke-linecap="round"/></svg>
  <p class="side" style="left:80px;top:118px;transform:rotate(-14deg);font-style:italic;font-weight:700;font-size:5.6px;z-index:4">Jeder<br>Neukunde<br>bekommt:<br><span style="font-size:8px">€ 100,-<br>GESCHENKT!</span></p>
  <p class="foot" style="left:12px;top:188px;font-size:5.6px;font-weight:500">... mit dem guten Gefühl, dass alles sauber<br>ist – ab in den Urlaub!</p>
</article>

<article class="post" style="left:427px;top:968px">
  <div class="hdr"></div><div class="logo"><i></i>Putzwerk<br>Pioniere</div>
  <h2 class="title">REINIGUNGS<br>SERVICE</h2>
  <div class="band" style="height:176px;border-radius:0 80px 0 0/0 30px 0 0"></div>
  <div class="pill" style="left:32px;width:136px;padding:9px 0 0 26px;font-size:7.8px">Ihr Garten – wir<br>kümmern uns darum!</div>
  <div class="ph" role="img" aria-label="Gelbe Gießkanne mit Gänseblümchen" style="left:8px;top:90px;width:52px;height:54px;border-radius:40% 50% 20% 30%;background:linear-gradient(135deg,#f4d34a,#e0b62a);z-index:2"></div>
  <div class="ph" style="left:48px;top:98px;width:116px;height:18px;border-radius:9px;background:var(--blue-light);z-index:2"></div>
  <p class="foot" style="left:56px;top:102px;font-size:6.6px;font-weight:700">Wir übernehmen für Sie:</p>
  <svg style="position:absolute;left:60px;top:124px;z-index:3" width="10" height="40" viewBox="0 0 10 40"><g fill="#fff"><circle cx="5" cy="4" r="3.5"/><circle cx="5" cy="16" r="3.5"/><circle cx="5" cy="28" r="3.5"/></g><g fill="none" stroke="#6fa6ca" stroke-width="1.2"><path d="M3 4 L4.5 5.5 L7 2.5"/><path d="M3 16 L4.5 17.5 L7 14.5"/><path d="M3 28 L4.5 29.5 L7 26.5"/></g></svg>
  <p class="foot" style="left:74px;top:124px;font-size:6.6px;font-weight:500;line-height:1.8">Rasenmähen<br>Pflanzen gießen<br>Unkraut entfernen</p>
  <div class="ph" role="img" aria-label="Gänseblümchen am Boden" style="left:0;top:164px;width:100px;height:22px;border-radius:10px;background:linear-gradient(90deg,#8ab7d4,#f4f0d0,#8ab7d4);z-index:2"></div>
  <p class="foot" style="left:58px;top:190px;font-size:6px">Jetzt Termin vereinbaren!</p>
</article>

<article class="post" style="left:622px;top:968px">
  <div class="ph" style="left:0;top:0;width:165px;height:58px;background:var(--blue);border-radius:0 0 50% 50%/0 0 22px 22px"></div>
  <h2 class="title" style="left:0;width:165px;text-align:center;top:18px">REINIGUNGS<br>SERVICE</h2>
  <div class="ph" style="left:0;top:60px;width:165px;height:148px;background:linear-gradient(180deg,#ffffff,#e3eef6)"></div>
  <div class="ph" style="left:62px;top:96px;width:40px;height:40px;background:var(--navy);z-index:2"></div>
  <p class="side" style="left:0;width:165px;text-align:center;top:142px;font-size:13px;font-weight:800;color:var(--navy);line-height:1.05">Putzwerk<br>Pioniere</p>
  <p class="side" style="left:0;width:165px;text-align:center;top:188px;font-size:5px;font-weight:700;color:var(--navy)">Sauberkeit ist unsere<br>Leidenschaft</p>
</article>

</main>
</body>
</html>
```